A QUIET AMBER PRIMER ON RANKS

subtitle: AN INTRO TO SEARCH ENGINE OPTIMIZATION
background: white
dimensions: 1562x2500

Target Market(s)

Marketing professionals

Industry/Entity Type

Digital Marketing

Font styles to use
Sans Serif

Colors
ffffff
1b1b1b
3176b5

Requirements
Should not have
• Images or graphics

```html
<!DOCTYPE html>
<html lang="en">
<head>
<meta charset="utf-8">
<title>A Quiet Amber Primer on Ranks</title>
<link rel="stylesheet" href="https://fonts.googleapis.com/css2?family=Cinzel:wght@400;600&family=Open+Sans:wght@400;800&display=swap">
<style>
  :root {
    --paper: #e9e6dd;
    --paper-band: #f1efe7;
    --paper-foot: #f4f1df;
    --ink: #111111;
    --ink-navy: #1b2540;
    --letter-black: #1b1b1b;
    --letter-grey: #7e7e7e;
    --letter-blue: #1f62ab;
    --white: #ffffff;
  }
  html, body {
    margin: 0;
    padding: 0;
    overflow: hidden;
    background: var(--white);
  }
  .cover {
    position: relative;
    width: 800px;
    height: 1200px;
    overflow: hidden;
    background: var(--paper);
    font-family: "Cinzel", Georgia, serif;
    color: var(--ink);
  }
  .kicker {
    position: absolute;
    top: 38px;
    left: 0;
    width: 100%;
    text-align: center;
    font-size: 21px;
    font-weight: 600;
    letter-spacing: 2px;
    color: var(--ink-navy);
  }
  .title-band {
    position: absolute;
    top: 80px;
    left: 0;
    width: 100%;
    height: 158px;
    background: var(--paper-band);
  }
  .rule {
    position: absolute;
    left: 80px;
    width: 642px;
    height: 3px;
    background: var(--ink);
  }
  .rule--top { top: 77px; }
  .rule--bottom { top: 236px; }
  .title {
    position: absolute;
    top: 96px;
    left: 0;
    width: 100%;
    margin: 0;
    text-align: center;
    font-weight: 400;
    font-size: 43px;
    line-height: 72px;
    letter-spacing: 1px;
  }
  .acronym {
    position: absolute;
    top: 260px;
    left: 0;
    width: 800px;
    height: 820px;
  }
  .acronym .big {
    font-family: "Open Sans", Arial, sans-serif;
    font-weight: 800;
    text-anchor: middle;
    filter: drop-shadow(0 0 3px var(--white)) drop-shadow(0 0 4px var(--white));
  }
  .acronym .word {
    font-family: "Open Sans", Arial, sans-serif;
    font-weight: 400;
    fill: var(--white);
    text-anchor: middle;
  }
  .footer-band {
    position: absolute;
    top: 1098px;
    left: 0;
    width: 100%;
    height: 102px;
    background: var(--paper-foot);
  }
  .author {
    position: absolute;
    top: 1120px;
    left: 0;
    width: 100%;
    text-align: center;
    font-size: 40px;
    font-weight: 600;
    letter-spacing: 7px;
    color: var(--ink-navy);
  }
</style>
</head>
<body>
<main class="cover">
  <div class="title-band"></div>
  <p class="kicker" style="margin:0">An Introduction to SEO</p>
  <div class="rule rule--top"></div>
  <h1 class="title">A QUIET AMBER PRIMER<br>ON RANKS</h1>
  <div class="rule rule--bottom"></div>

  <svg class="acronym" viewBox="0 260 800 820" xmlns="http://www.w3.org/2000/svg">
    <defs>
      <path id="optimisation-arc" d="M 286 968 A 114 114 0 0 1 514 968"/>
    </defs>
    <text class="big" x="400" y="511" font-size="325" fill="var(--letter-black)">S</text>
    <text class="word" x="400" y="405" font-size="25">SEARCH</text>

    <text class="big" x="400" y="778" font-size="314" fill="var(--letter-grey)">E</text>
    <text class="word" x="400" y="667" font-size="25">ENGINE</text>

    <text class="big" x="400" y="1048" font-size="325" fill="var(--letter-blue)">O</text>
    <text class="word" font-size="23">
      <textPath href="#optimisation-arc" startOffset="50%">OPTIMISATION</textPath>
    </text>
  </svg>

  <div class="footer-band"></div>
  <p class="author" style="margin:0">AUTHOR NAME</p>
</main>
</body>
</html>
```